Meadowlark Lane Yoga Facebook Design

"Practice Radiant Movement"

Foundational and sustainable yoga practice to cultivate growth through a variety of anatomy- informed movement patterns. Develop an informative and inspirational connection with the mind, body and spirit, through smart and integrated movement.

-I need a design that is happy and cheerful and attracts children and adults alike. I teach vinyassa based yoga that is sustainable and smart, kid yoga, and chair yoga.

-A movement practic rooted in foundation, core, and expression

- Accessible yoga for a sustained practice. A guided movement practice where one gains information and knowledge of oneself through a mind/body connection. For one feel good physically with a new awareness of their internal radiance that exists in all beings. Physical rejuvenation egnites a light and increases energy to flow through the physical body, which ultimately tranlates into works of kindness for others and out in the world.

Nora Whitfield
Yoga Instructor
MD, Pediatrician
RYT-200
RCYT
Certified yoga teacher for adults and children

Full description:
What is the positioning or mission statement of your company? to guide individuals in a yoga-based safe and sustainable movement practice applicable to all ages and body types. Currently my focus is working with children in daycare and school settings, but my goal is to expand into private yoga practice for adults, and potentially as part of rented space in studios. I hope to find a way to work with children AND adults (so would love for logo to be appealing to both), but current focus is with children based on need and demand in the community. yoga for children also compliments my backround as a pediatrician/neonatologist, and I greatly miss interacting with children. I also want to emphasize a yoga/movement practice that is focused more on what one feels internally through movement. NOT what one looks like asthetically. I believe in removing all mirrors from yoga/movement practice. It should be an experience of movement/poses/yoga through appropriate cueing and education. It is not about the details of how far the knee should bend, or how high the leg should be. Focusing on foudation first, core, then core engagement and ultimately expression of poses/movements. A focus on strength, stability and mobility, not just flexibility, which is the common perception/association with yoga. I also want individuals to learn to be an advocate of their own health. Through guidance, I hope for individuals to connect with their body so they know themselves so well to be able to advocate for themselves in the modern healthcare world. This internal experience and connection is so essential in a world where modern medicine has become a business and it is all about making a dollar. the connection with patients is lost, and individuals need to learn to empower themselves and through their new found voice to be able to articulate what is wrong.
Does your company have a tagline or slogan that should be included with the logo? "Practice Radiant Movement"
What do you hope your company can be known for? Accessible yoga for a sustained practice. A guided movement practice where one gains information and knowledge of oneself through a mind/body connection. For one feel good physically with a new awareness of their internal radiance that exists in all beings. Physical rejuvenation egnites a light and increases energy to flow through the physical body, which ultimately tranlates into works of kindness for others and out in the world.
What color palettes might you prefer? why? love the colors currently chosen
Where will the logo be primarily used? initially business cards, but hopefully future websites, t-shirts, and potentially local magazine adds. Also starting with a small couple of banners for community events in the area. I currently practice as a nomad out of my car :)
Are there any elements you would prefer to see in the logo? Movement. A modern depiction of a human body/figure practicing movement. Hoping to avoid a stereotypical yoga pose per say, just because I want to people to think of it more of a movement practice with yoga roots. Modern yoga. There are elements of breathing and connecting with oneself through the flow of breath and movement, but I do not focus on the meditative/cerebral aspect of the yoga practice. What I teach is almost reaching a meditative state through movement. I personally don't practice, nor resonate with just seated meditation. just not my thing :)
In your opinion, what defines a well-designed logo? curiosity. enough info for individuals to think they know what it means, but want to know more. invokes curiosity, but not too abstract. Reproducible. not too complicated. I want also to invoke a community feel, so a design that appeals to all people within a community.
What is your preference in reference to icons, typography, spokespeople (characters), etc.? modern design. I love the idea of a logo for my purposes, to invoke a sense of movement from within. So not too static.
What words or icons must be included in the logo? movement with yoga roots.
What logos do you like and why? A representation, but not exact. I think some ambiguity is intriguing for others, and also memorable. I want it to be an artistic representation of movement/yoga
What logos do you dislike and why? too busy, too loud.
In your opinion, what is the primary purpose for a logo? association
Who is the primary target audience? (who is most likely to use your services/product?) Children and their parents, but ultimately to expand into teaching adults. I even have aspirations of prenatal and post-natal yoga. Potentially incorporating infants.
Who currently uses your product the most? n/a (working in schools/daycare currently. It is currently all volunteer)
Are you pleased with the range of people your company serves? n/a
Are you looking to expand, modify, or completely change your target audience? or will it remain the same? yes! expand into an adult audience.
How do you plan to focus on your target audience? currently by working through schools and daycares. hopefully ultimately through after school care programs and then offering kid yoga in an existing yoga studio (working on this with Q studio in Ridgeland, currently)
What are your main forms of advertising? word of mouth, schools, daycares. Happy kids talking to their parents about the yoga class they took and happy teachers :)
How do most customers find out about your company?
Which gender are you targeting? All genders! However, with kid yoga, often the maternal individual in the child's life is more involved with decision making as far as extracurricular activities

Target Market(s)

Adults, children and families interested in movement, wellness and fun

Font styles to use
Sans Serif

Requirements
Must have
• ***I meant to emphasize the that "S" figure in my logo is SOOO iimportant to me. My daughter designed it. please highlight the "S" figure if possible******
My logo and the phrase "practice radiant movement"
Same colors as my logo
Feel like movement and fun.
Attracts children and families
Incorporate pieces of my description somehow
Nice to have
• different yoga poses or figures in movement
abstract design
attacts all body types and genders
inclusive

Industry is yoga, movement, wellness
Should not have
• no darkness
want happy and vibrant, inviting

```html
<!DOCTYPE html>
<html lang="en">
<head>
<meta charset="utf-8">
<title>Meadowlark Lane Yoga – Facebook Cover</title>
<link rel="stylesheet" href="https://fonts.googleapis.com/css2?family=Amatic+SC:wght@400;700&display=swap">
<style>
  :root {
    --page-bg: #efefef;
    --sun-yellow: #f5d838;
    --pool-teal: #62c7cf;
    --photo-warm-top: #a06a5c;
    --photo-warm-mid: #d9b7a4;
    --photo-floor: #e6d3b4;
    --logo-ink: #ffffff;
  }
  html, body {
    margin: 0;
    padding: 0;
    width: 1200px;
    height: 1200px;
    overflow: hidden;
    background: var(--page-bg);
  }
  .cover {
    position: absolute;
    left: 40px;
    top: 354px;
    width: 1120px;
    height: 491px;
    border-radius: 12px;
    overflow: hidden;
    font-family: "Amatic SC", sans-serif;
  }
  .class-photo {
    position: absolute;
    inset: 0;
    background:
      linear-gradient(180deg, var(--photo-warm-top) 0%, #b88478 22%, var(--photo-warm-mid) 48%, var(--photo-floor) 100%);
  }
  .class-photo::after {
    content: "";
    position: absolute;
    inset: 0;
    background: linear-gradient(90deg, rgba(255,190,150,0.25) 0%, rgba(255,140,60,0.18) 50%, rgba(255,255,255,0) 100%);
  }
  .brand-shapes {
    position: absolute;
    inset: 0;
    width: 100%;
    height: 100%;
    z-index: 1;
  }
  .brand-name-feature {
    position: absolute;
    z-index: 2;
    left: 741px;
    top: 58px;
    width: 260px;
    text-align: center;
    color: var(--pool-teal);
    font-weight: 700;
    font-size: 64px;
    line-height: 0.95;
    margin: 0;
  }
  .tagline {
    position: absolute;
    z-index: 2;
    left: 610px;
    top: 440px;
    width: 482px;
    margin: 0;
    color: var(--sun-yellow);
    font-weight: 400;
    font-size: 31px;
    letter-spacing: 4.2px;
    text-transform: uppercase;
    white-space: nowrap;
  }
  .corner-mark {
    position: absolute;
    z-index: 2;
    left: 22px;
    top: 438px;
    display: flex;
    align-items: center;
    gap: 6px;
  }
  .corner-mark .dot {
    width: 14px;
    height: 14px;
    border-radius: 50%;
    background: var(--sun-yellow);
  }
  .corner-mark .name {
    color: var(--logo-ink);
    font-weight: 700;
    font-size: 20px;
  }
</style>
</head>
<body>
  <section class="cover">
    <div class="class-photo" role="img" aria-label="Photo of a group yoga class doing a side stretch on colourful mats in a sunlit hall"></div>

    <svg class="brand-shapes" viewBox="0 0 652 286" preserveAspectRatio="none" aria-hidden="true">
      <circle cx="545" cy="150" r="205" fill="var(--sun-yellow)"/>
      <path d="M310,286 C300,260 320,235 345,225 C380,200 420,165 470,160 C560,150 620,170 652,185 L652,286 Z" fill="var(--pool-teal)"/>
      <circle cx="642" cy="95" r="18" fill="var(--pool-teal)"/>
      <circle cx="372" cy="171" r="8" fill="var(--pool-teal)"/>
      <circle cx="603" cy="139" r="9" fill="var(--pool-teal)"/>
      <circle cx="295" cy="206" r="10" fill="var(--pool-teal)"/>
      <circle cx="271" cy="232" r="6" fill="var(--pool-teal)"/>
      <circle cx="293" cy="263" r="10" fill="var(--pool-teal)"/>
      <circle cx="378" cy="24" r="6" fill="var(--sun-yellow)"/>
      <circle cx="335" cy="44" r="5" fill="var(--sun-yellow)"/>
      <circle cx="326" cy="89" r="8" fill="var(--sun-yellow)"/>
      <circle cx="331" cy="152" r="6" fill="var(--sun-yellow)"/>
      <circle cx="618" cy="211" r="13" fill="var(--sun-yellow)"/>
    </svg>

    <p class="brand-name-feature">Meadowlark<br>Lane<br>Yoga</p>

    <p class="tagline">Practice Radiant Movement</p>

    <div class="corner-mark">
      <span class="dot"></span>
      <span class="name">Meadowlark Lane Yoga</span>
    </div>
  </section>
</body>
</html>
```